Blog Banner Design Project: Harbour Lantern Guides

Looking for a new banner for my blog " Owen Pelsworth's Harbour Lantern Guides" at http://www.harbourlanternguides-demo.net - and once design agreed also want an updated album art for the podcast that goes along with the site.
For more about the blog and what it is about:
http://www.harbourlanternguides-demo.net/about
Harbour Lantern Guides is a Luxury Travel Blog And Podcast that provides inspiration, advice and tips about luxurious travel experiences, including destinations, transportation, accommodation, and journeys, that travellers can read, listen to or watch.
Objective of the new design
(1) retain the colour scheme ideally to retain the brand identity, as have been using these colours since 2005.
(2) introduce more of my personality and make it more visually and overt that it is "Owen Pelsworth's Harbour Lantern Guides", so possibly introducing my image into the blog banner so visitors are clear and more aware of the person behind the brand.
(3) needs to have an up-market, luxury but modern feel.
(4) if possible reflect the focus on the content (destinations, transportation, accommodation, attractions and journeys) - but this maybe best left to just words as want the design to be bold and more of the branding and personality.
Ideal wording
Smallish: Owen Pelsworth's
Main wording: Harbour Lantern Guides
Sub-title/ small: luxurious destinations, transportation, accommodation and journeys.
I have a poll running with readers of my blog to rate the designs to help me to chose the final route, and so there is no need to submit any more designs. I will make the decision once the poll closes on the weekend.

```html
<!DOCTYPE html>
<html lang="en">
<head>
<meta charset="utf-8">
<title>Owen Pelsworth's Harbour Lantern Guides – Blog Banner</title>
<link rel="stylesheet" href="https://fonts.googleapis.com/css2?family=Lato:ital,wght@0,900;1,400;1,700&display=swap">
<style>
  :root {
    --bg-black: #000000;
    --tab-magenta: #b3179c;
    --tab-magenta-light: #cc2db3;
    --tab-text: #f6d3ef;
    --title-white: #ffffff;
    --tagline-grey: #7a7a7a;
    --glow-orange: #f28c00;
    --glow-yellow: #ffd21a;
    --portrait-blue: #4f9fd6;
    --portrait-sky: #9fd0ef;
    --portrait-skin: #d9a58a;
  }

  * { margin: 0; padding: 0; box-sizing: border-box; }

  html, body {
    width: 1200px;
    height: 172px;
    overflow: hidden;
    background: var(--bg-black);
  }

  .banner {
    position: relative;
    width: 1200px;
    height: 172px;
    background: var(--bg-black);
    overflow: hidden;
    font-family: "Lato", Arial, sans-serif;
  }

  .host-portrait {
    position: absolute;
    left: 0;
    top: 0;
    width: 192px;
    height: 172px;
    background:
      radial-gradient(ellipse 38% 34% at 48% 40%, var(--portrait-skin) 0%, var(--portrait-skin) 60%, transparent 100%),
      linear-gradient(180deg, var(--portrait-sky) 0%, var(--portrait-blue) 100%);
    -webkit-mask-image: linear-gradient(90deg, #000 78%, transparent 100%);
            mask-image: linear-gradient(90deg, #000 78%, transparent 100%);
  }

  .host-tab {
    position: absolute;
    left: 0;
    top: 0;
    width: 370px;
    height: 56px;
  }

  .host-name {
    position: absolute;
    left: 78px;
    top: 10px;
    font-style: italic;
    font-weight: 700;
    font-size: 25px;
    line-height: 32px;
    color: var(--tab-text);
    white-space: nowrap;
  }

  .site-title {
    position: absolute;
    left: 226px;
    top: 52px;
    font-weight: 900;
    font-size: 70px;
    line-height: 84px;
    letter-spacing: -0.5px;
    color: var(--title-white);
    white-space: nowrap;
  }

  .glow-bar {
    position: absolute;
    left: 190px;
    top: 150px;
    width: 770px;
    height: 22px;
    background:
      radial-gradient(ellipse 60% 90% at 50% 100%, var(--glow-yellow) 0%, var(--glow-orange) 55%, transparent 100%);
  }

  .glow-bar::before {
    content: "";
    position: absolute;
    left: 0;
    right: 0;
    top: 2px;
    height: 3px;
    background: linear-gradient(90deg, transparent 0%, var(--glow-orange) 15%, var(--glow-yellow) 50%, var(--glow-orange) 85%, transparent 100%);
  }

  .tagline {
    position: absolute;
    left: 1030px;
    top: 20px;
    width: 150px;
    font-style: italic;
    font-weight: 400;
    font-size: 17px;
    line-height: 21px;
    text-align: center;
    color: var(--tagline-grey);
  }
</style>
</head>
<body>
  <header class="banner">
    <div class="host-portrait" role="img" aria-label="Portrait photo of the blog host smiling, wearing a light blue shirt"></div>

    <svg class="host-tab" viewBox="0 0 370 56" aria-hidden="true">
      <defs>
        <linearGradient id="tabFill" x1="0" y1="0" x2="1" y2="0">
          <stop offset="0" stop-color="var(--tab-magenta-light)"/>
          <stop offset="1" stop-color="var(--tab-magenta)"/>
        </linearGradient>
      </defs>
      <polygon points="0,0 370,0 352,56 0,56" fill="url(#tabFill)"/>
    </svg>
    <p class="host-name">Owen Pelsworth's</p>

    <h1 class="site-title">Harbour Lantern Guides</h1>

    <div class="glow-bar" aria-hidden="true"></div>

    <p class="tagline">“Luxurious destinations, transportation, accommodation and journeys.”</p>
  </header>
</body>
</html>
```